Marlow Cat Lodge needs a website and a logo :)

I need a web design for my pet hotel. I will use it in Wordpress, probable with Elementor, so if you can also offer the WP template creation, that's a bonus but I don't wanna book the coded-website option here as I don't think that applies to WP. It would be great if you come up with a logo as well.

Here some info:

Modern, premium cat boarding with a vet on-site

Marlow Cat Lodge is a boutique cat boarding facility in Nelson, New Zealand, offering high-quality, vet-supervised care for all cats, including those with special medical needs. Unlike standard catteries, we focus on low-stress boarding, with separate spaces for special-needs and healthy cats, ensuring a safe, comfortable, and peaceful environment. We also prioritize convenience with self check-in and check-out, leveraging technology to enhance the experience.

Target Market(s)

Cat owners for short term to long term stays that don't want the cheapest option and will value that we have a vet on-site

Industry/Entity Type

cat boarding

Number of Pages Required

5+ page

Font styles to use
Sans Serif
Other font styles liked:
• Nothing that needs installation or a license. Please use Google Fonts.

Requirements
Must have
• Landing page, about us, services, blog and contact page - the landing page should have the typical sales layout with hero image top right, a tag line "Modern, premium cat boarding with a vet on-site" and 2 paragraphs. Paragraph 1 (Problem): Leaving your cat behind can be stressful, especially if they need special care. Standard catteries often lack vet oversight and a calm, tailored environment. Paragraph 2 (Solution): At Marlow Cat Lodge, we offer premium, vet-supervised boarding with separate spaces for special-needs and healthy cats. Our self check-in and tech-driven system makes drop-offs and pick-ups effortless... you know the drill :)
Nice to have
• Ask ChatGPT for some ideas and give it the business plan: https://files.example-docs.net/document/d/7qerTy_LKMWBP2hfsx8V304UiLoXyOpqRkZjTnWaBcD/edit?usp=sharing
Should not have
• NO DOGS :)

```html
<!DOCTYPE html>
<html lang="en">
<head>
<meta charset="utf-8">
<title>Marlow Cat Lodge – Website Pages</title>
<link href="https://fonts.googleapis.com/css2?family=Poppins:wght@300;400;500;600;700;800&display=swap" rel="stylesheet">
<style>
:root{
  --blue:#0d6fd3;
  --blue-deep:#0a5bb0;
  --ink:#2b3038;
  --heading:#4b525b;
  --muted:#6f7580;
  --light:#f0f1f3;
  --line:#e2e5ea;
  --board:#8796a1;
  --white:#ffffff;
}
*{box-sizing:border-box;margin:0;padding:0}
html,body{width:1178px;height:1200px;overflow:hidden;background:var(--board)}
body{font-family:'Poppins',sans-serif;color:var(--ink)}
.board{position:absolute;left:0;top:0;width:1904px;height:1940px;transform:scale(.6187);transform-origin:0 0}
.page{position:absolute;width:444px;background:var(--white);overflow:hidden}
.page--home{left:38px;top:41px;height:1854px}
.page--about{left:500px;top:41px;height:1265px}
.page--services{left:962px;top:41px;height:1310px}
.page--blog{left:1424px;top:41px;height:794px}
.page--contact{left:1424px;top:857px;height:806px}
section{position:relative}

/* header */
.site-header{height:34px;display:flex;align-items:center;padding:0 42px;background:var(--white)}
.brand{display:flex;align-items:center;gap:4px;font-size:9px;font-weight:400;color:var(--blue);white-space:nowrap}
.brand-dot{width:9px;height:9px;border-radius:50%;border:1px solid var(--blue)}
.nav{display:flex;gap:11px;margin-left:auto;font-size:4.2px;color:var(--ink)}
.nav .active{color:var(--blue)}
.loc{display:flex;align-items:center;gap:3px;margin-left:11px;font-size:3.8px;line-height:1.3}
.loc b{color:var(--blue);font-weight:600;display:block}
.pin{width:9px;height:9px;border-radius:50%;background:var(--blue);display:flex;align-items:center;justify-content:center}

/* common type */
.eyebrow{font-size:4.2px;font-weight:600;color:var(--blue);text-transform:uppercase;letter-spacing:.2px}
.h2{font-size:11px;font-weight:600;color:var(--heading);text-transform:uppercase;line-height:1.15}
.h2--blue{color:var(--blue);font-weight:700}
.p{font-size:4.2px;line-height:1.6;color:var(--muted)}
.center{text-align:center}
.btn{display:inline-block;background:var(--blue);color:var(--white);font-size:3.8px;font-weight:700;text-transform:uppercase;padding:3px 7px;border-radius:2px}
.btn--ghost{background:transparent;border:.6px solid var(--white)}
.btn--line{background:transparent;border:.6px solid #9aa7b3;color:#5b6b7a}
.photo{position:absolute}
.blob{border-radius:58% 42% 48% 52%/44% 52% 48% 56%}
.round{border-radius:50%;border:2px solid var(--blue)}
/* flat photo fills */
.tone-cat{background:linear-gradient(135deg,#2a6cc0,#5f9bd8 60%,#c9b08f)}
.tone-room{background:linear-gradient(120deg,#f1f1f1,#d6d8db 50%,#a9a49b)}
.tone-face{background:linear-gradient(160deg,#cfd8e2,#5a6f88)}
.tone-dark{background:linear-gradient(160deg,#3a3b3f,#1c1d20)}
.tone-family{background:linear-gradient(160deg,#a7bacd,#6a8299)}
.tone-vet{background:linear-gradient(135deg,#f2f3f5,#d2d9e0 60%,#bfa58a)}
.tone-kitten{background:linear-gradient(135deg,#e8ecf1,#b5bec8)}
.tone-map{background:linear-gradient(135deg,#eceef1,#dfe6e3)}

/* hero band on inner pages */
.page-hero{height:165px;color:var(--white)}
.page-hero .photo{inset:0;background:linear-gradient(100deg,#2365ad 0%,#2f6fb0 40%,#5f7c98 70%,#55697d)}
.page-hero .hero-text{position:absolute;left:42px;top:56px;width:150px}
.page-hero h1{font-size:11px;font-weight:700;letter-spacing:.3px}
.page-hero p{font-size:4.2px;line-height:1.6;margin-top:5px;opacity:.95}

/* cats strip */
.cats-strip{height:80px}
.cats-strip .photo{left:60px;right:50px;top:12px;bottom:0;border-radius:30px 30px 0 0;background:linear-gradient(180deg,#d7cab8,#8f8070)}

/* blue cta */
.cta-band{background:var(--blue);color:var(--white);display:flex;align-items:center;justify-content:space-between;padding:0 42px}
.cta-band h3{font-size:9px;font-weight:700;letter-spacing:.2px}
.cta-plain{display:flex;align-items:center;justify-content:space-between;padding:0 42px;border-bottom:1px solid var(--line)}
.cta-plain h3{font-size:9px;font-weight:700;color:#5b6b7a}

/* footer */
.site-footer{display:grid;grid-template-columns:128px 63px 82px 1fr;padding:22px 42px 0;position:relative}
.site-footer .brand{font-size:10px;margin-bottom:6px}
.site-footer h4{font-size:4.4px;font-weight:700;color:var(--ink);margin-bottom:4px}
.site-footer li{list-style:none;font-size:3.7px;line-height:1.9;color:var(--muted)}
.site-footer .p{font-size:3.7px;padding-right:20px}
.socials{display:flex;gap:2px;margin-top:3px}
.socials i{width:6px;height:6px;border-radius:50%;background:var(--blue);display:block}
.copyright{position:absolute;left:0;right:0;bottom:10px;text-align:center;font-size:3.4px;color:var(--muted)}

/* pre-book form */
.prebook{background:var(--blue);color:var(--white);padding-top:30px}
.prebook h2{font-size:14px;font-weight:700;text-align:center;letter-spacing:.3px}
.form-grid{width:320px;margin:14px auto 0;display:grid;grid-template-columns:repeat(4,1fr);gap:7px 4px}
.field{background:var(--white);height:14px;border-radius:1px;font-size:3.6px;color:var(--muted);display:flex;align-items:center;justify-content:space-between;padding:0 4px}
.field--half{grid-column:span 2}
.option-title{text-align:center;font-size:6px;font-weight:600;text-decoration:underline;margin-top:10px}
.options{display:flex;justify-content:center;gap:12px;font-size:3.4px;margin-top:5px}
.options span::before{content:"";display:inline-block;width:4px;height:4px;border-radius:50%;background:var(--white);margin-right:3px;vertical-align:middle}
.textarea{width:320px;height:42px;margin:9px auto 0;background:var(--white);border-radius:2px;padding:6px;font-size:3.6px;color:var(--ink)}
.textarea small{display:block;color:#99a;font-size:3.4px;margin-top:2px;padding-left:6px}
.submit{display:block;width:30px;margin:8px auto 0;text-align:center;font-size:3.4px;font-weight:700;background:var(--white);color:var(--blue);padding:2px 0;border-radius:1px}

/* home hero */
.home-hero{height:202px;background:linear-gradient(90deg,#f6f6f6,#ececec)}
.home-hero h1{position:absolute;left:42px;top:35px;font-size:18px;line-height:20px;font-weight:800;color:var(--blue-deep);letter-spacing:.2px}
.ticks{position:absolute;left:42px;top:82px;list-style:none}
.ticks li{font-size:4.6px;color:var(--ink);margin-bottom:7px;display:flex;align-items:center;gap:4px}
.ticks li::before{content:"";width:5px;height:5px;border-radius:50%;background:var(--blue)}
.home-hero .btn{position:absolute;left:42px;top:128px}

/* service cards */
.service-cards{position:absolute;left:42px;top:106px;display:flex;gap:14px}
.card{width:110px;height:212px;background:var(--white);border-radius:4px;box-shadow:0 1px 6px rgba(0,0,0,.13);padding:34px 7px 0;text-align:center;position:relative}
.card .photo{left:33px;top:-20px;width:44px;height:44px;border-radius:50%;border:2px solid var(--white)}
.card h3{font-size:4.6px;font-weight:700;color:var(--blue);margin-bottom:5px}
.card h4{font-size:4.2px;font-weight:600;color:var(--ink);margin-top:5px}
.card p{font-size:3.5px;line-height:1.5;color:var(--muted);margin-top:2px}
.card hr{border:0;border-top:.5px solid var(--line);margin-top:4px}
.card .btn{position:absolute;left:50%;transform:translateX(-50%);bottom:9px}

/* features */
.features{position:absolute;left:54px;top:195px;display:flex;gap:22px}
.feature{width:100px}
.feature .icon{width:22px;height:22px;border-radius:50%;background:#dbe7f4;margin-bottom:7px;display:flex;align-items:center;justify-content:center}
.feature h4{font-size:4px;font-weight:700}
.feature p{font-size:3.8px;line-height:1.55;color:var(--muted)}

/* team */
.member{position:absolute;width:215px}
.member .eyebrow{margin-bottom:4px}
.member .p{font-size:3.7px}
.member--right{text-align:right}
.portrait{position:absolute;width:92px;height:92px}

/* service grid */
.svc-grid{position:absolute;left:64px;display:grid;grid-template-columns:repeat(3,112px);row-gap:10px}
.svc-grid h4{font-size:4.4px;font-weight:500;color:#5b6370;display:flex;align-items:center;gap:2px}
.svc-grid h4::before{content:"";width:4px;height:4px;border-radius:50%;background:#6a7380;flex:none}
.svc-grid p{font-size:3.5px;line-height:1.5;color:var(--muted);width:98px;margin-top:2px}

/* blog */
.post-meta{font-size:3.4px;color:var(--blue);display:flex;gap:6px}
.post-title{font-size:4.8px;font-weight:700;color:var(--ink);margin:3px 0}
.mini{display:flex;gap:4px;height:58px;border:.5px solid var(--line);margin-bottom:4px;overflow:hidden}
.mini .thumb{width:76px;height:100%;flex:none}
.mini .post-title{font-size:4.2px;margin:1px 0}
.mini .p{font-size:3.3px;line-height:1.5}

.info-item{display:flex;gap:6px;align-items:flex-start;margin-bottom:8px}
.info-item .pin{width:11px;height:11px;flex:none}
.info-item b{display:block;font-size:4.2px;font-weight:500;color:var(--blue)}
.info-item span{font-size:3.8px;color:var(--ink)}
</style>
</head>
<body>
<div class="board">

<!-- HOME -->
<div class="page page--home">
  <header class="site-header">
    <div class="brand"><span class="brand-dot"></span>Marlow Cat Lodge</div>
    <nav class="nav"><span class="active">Home</span><span>About us</span><span>Our Services</span><span>Latest blog</span><span>Contact Us</span></nav>
    <div class="loc"><span class="pin"><svg width="5" height="5" viewBox="0 0 10 10"><path d="M5 1a3 3 0 0 1 3 3c0 2-3 5-3 5S2 6 2 4a3 3 0 0 1 3-3z" fill="#fff"/></svg></span><div><b>LOCATIONS</b>New Zealand</div></div>
  </header>

  <section class="home-hero">
    <h1>VET OWNED<br>CAT RETREAT</h1>
    <ul class="ticks"><li>Compassionate Care</li><li>Expert Guidance</li><li>Personalized Support</li></ul>
    <span class="btn">Free book now</span>
    <div class="photo blob tone-room" style="left:229px;top:23px;width:160px;height:142px" role="img" aria-label="Vet sitting in a chair holding a cat in a bright room"></div>
  </section>

  <section style="height:358px">
    <div class="center" style="padding-top:30px">
      <div class="eyebrow">What we do</div>
      <div class="h2" style="margin-top:3px">Our Services</div>
      <p class="p" style="width:320px;margin:5px auto 0;font-size:3.6px">We offer a variety of boarding, comfort, and premium services, providing a stress-free, vet-supervised experience for every cat. Basic veterinary care can be provided on-site, while more complex treatments are handled at the local clinic for the best possible care.</p>
    </div>
    <div class="service-cards">
      <div class="card">
        <div class="photo tone-cat" role="img" aria-label="Ginger cat portrait"></div>
        <h3>BOARDING SERVICES</h3>
        <h4>Standard Cat Boarding</h4><p>Spacious, full-height enclosures with cozy bedding, a scratching post, and a cat tree.</p><hr>
        <h4>Premium Cat Boarding</h4><p>Extra-large suites with private outdoor access, and more space for relaxation.</p><hr>
        <h4>Special-Needs Boarding</h4><p>Dedicated suites for elderly, unvaccinated, or medically fragile cats.</p><hr>
        <h4>Multi-Cat Family Boarding</h4><p>Connected suites available for cats from the same household.</p>
        <span class="btn">View more</span>
      </div>
      <div class="card">
        <div class="photo tone-kitten" role="img" aria-label="Kitten playing with a ball"></div>
        <h3>COMFORT &amp; WELLNESS</h3>
        <h4>Personalized Play Sessions</h4><p>One-on-one interactive time with trained staff, using toys or feather wands.</p><hr>
        <h4>Feline Spa Experience</h4><p>Gentle brushing, coat conditioning, and stress-free hygiene care.</p><hr>
        <h4>Custom Hideouts</h4><p>Special cozy hideaway setups in the suite for shy or nervous cats.</p><hr>
        <h4>Live Webcam Access</h4><p>Owners can check in on their cat anytime via a secure webcam feed.</p>
        <span class="btn">View more</span>
      </div>
      <div class="card">
        <div class="photo tone-vet" role="img" aria-label="Veterinarian holding a cat"></div>
        <h3>VETERINARY</h3>
        <h4>Weight Management</h4><p>Tailored diet plans with intake tracking and progress updates.</p><hr>
        <h4>Dental Health &amp; Oral Hygiene</h4><p>Vet-led teeth checks and tartar control.</p><hr>
        <h4>Medication Administration</h4><p>Safe and stress-free handling of prescribed pills or topical treatments.</p><hr>
        <h4>Hydration &amp; Supplements</h4><p>Ensuring proper hydration and vet-approved supplements if needed.</p>
        <span class="btn">View more</span>
      </div>
    </div>
  </section>

  <section style="height:300px;background:var(--light)">
    <div class="photo blob tone-cat" style="left:50px;top:37px;width:155px;height:128px" role="img" aria-label="Cat sitting inside a blue cat condo"></div>
    <div style="position:absolute;left:242px;top:36px;width:160px">
      <div class="eyebrow" style="font-size:3.8px">Our cozy cat cages</div>
      <div class="h2" style="margin-top:3px">Designed for comfort<br>and well-being</div>
      <div style="font-size:4.4px;font-weight:600;color:var(--blue);text-decoration:underline;margin-top:7px">MODEL 4</div>
      <ul style="list-style:none;font-size:4.4px;line-height:2.05;margin-top:3px">
        <li>• Larger 4 cat capacity</li><li>• Larger condo</li><li>• Separate litter area</li><li>• Integrated ventilation</li><li>• Depth 750mm</li>
      </ul>
      <span class="btn" style="margin-top:5px">View more cages</span>
    </div>
    <div class="features">
      <div class="feature"><div class="icon"><svg width="11" height="11" viewBox="0 0 12 12"><rect x="2" y="2" width="8" height="8" fill="none" stroke="#0d6fd3"/><path d="M2 6h8M6 2v8" stroke="#0d6fd3"/></svg></div><h4>Cozy and Enclosed:</h4><p>Cats prefer small, secure spaces that mimic their natural environment, giving a sense of security and comfort.</p></div>
      <div class="feature"><div class="icon"><svg width="11" height="11" viewBox="0 0 12 12"><path d="M1 9h10M3 9V4l6-2v7" fill="none" stroke="#0d6fd3"/></svg></div><h4>Tailored for Well-Being:</h4><p>Every aspect of the design has been crafted to enhance your cat's relaxation and happiness.</p></div>
      <div class="feature"><div class="icon"><svg width="11" height="11" viewBox="0 0 12 12"><circle cx="6" cy="6" r="4" fill="none" stroke="#0d6fd3"/><circle cx="6" cy="6" r="1.5" fill="#0d6fd3"/></svg></div><h4>Relaxing Sounds &amp; Pheromones:</h4><p>We use special sounds and pheromones to create a calming atmosphere that reduces stress.</p></div>
    </div>
  </section>

  <section style="height:385px">
    <div class="center" style="padding-top:36px">
      <div class="eyebrow">About</div>
      <div class="h2" style="margin-top:2px">Marlow Cat Lodge</div>
      <p class="p" style="width:320px;margin:5px auto 0">At Marlow Cat Lodge, we're more than just a boarding facility—we're a family-run, vet-supervised home away from home for your feline companions.</p>
    </div>
    <div class="portrait photo round tone-face" style="left:76px;top:90px" role="img" aria-label="Portrait of the lodge veterinarian"></div>
    <div class="member" style="left:188px;top:100px"><div class="eyebrow">Meet Helena – the vet &amp; cat whisperer</div><p class="p">Dr. Helena Varga is a highly experienced veterinarian with over 20 years in small animal medicine across Europe and New Zealand. With expertise in surgery, dentistry, and laboratory diagnostics, she ensures every cat receives expert care. Whether it's a healthy, elderly, or medically fragile cat, she provides the professional attention and compassion they need.</p></div>
    <div class="portrait photo round tone-dark" style="left:274px;top:185px" role="img" aria-label="Portrait of the operations lead"></div>
    <div class="member member--right" style="left:52px;top:200px"><div class="eyebrow">Meet Tomas – the tech &amp; operations expert</div><p class="p">With a background in IT, process optimization, and management, Tomas Brecker runs the technical and organizational side of Marlow Cat Lodge. From seamless online booking to a stress-free environment, he focuses on making everything run smoothly and creating a modern, premium boarding experience.</p></div>
    <div class="portrait photo round tone-family" style="left:76px;top:278px" role="img" aria-label="Family photo by a lake"></div>
    <div class="member" style="left:188px;top:295px"><div class="eyebrow">Our family team</div><p class="p">We believe a loving environment makes all the difference. Our teenage kids are part of the team, giving the cats extra playtime, cuddles, and attention. At Marlow Cat Lodge, we're providing peace of mind for owners and a second home for their pets.</p></div>
  </section>

  <section class="cats-strip" style="height:78px"><div class="photo" style="left:68px;top:8px" role="img" aria-label="Row of kittens peeking over the edge"></div></section>

  <section class="prebook" style="height:222px">
    <h2>CONTACT &amp; PRE-BOOK</h2>
    <div class="form-grid">
      <div class="field">Your name*</div><div class="field">Your cats name*</div><div class="field">Your email address*</div><div class="field">Your email address*</div>
      <div class="field field--half">Pre book a stay from <span>▢</span></div><div class="field field--half">Pre book a stay until <span>▢</span></div>
    </div>
    <div class="option-title">Boarding option</div>
    <div class="options"><span>Standard Condo ($30 / day)</span><span>Premium Condo ($50 / day)</span></div>
    <div class="textarea">General enquiry / additional information?<small>e.g. multiple cats, additional services...</small></div>
    <span class="submit">SUBMIT</span>
  </section>

  <section style="height:160px">
    <div class="photo" style="inset:0;background:#8e9297" role="img" aria-label="Street map around the lodge with a location marker"></div>
    <div class="photo tone-map" style="left:272px;top:55px;width:68px;height:68px;border-radius:50%" role="img" aria-label="Close-up map of the lodge location"></div>
    <p style="position:absolute;left:250px;top:126px;width:112px;text-align:center;font-size:3.8px;color:#fff">14 Harbour View Lane,<br>Nelson 7010</p>
  </section>

  <footer class="site-footer" style="height:115px">
    <div><div class="brand"><span class="brand-dot"></span>Marlow Cat Lodge</div><p class="p">Boutique, vet-supervised cat boarding in Nelson with calm suites and easy self check-in.</p></div>
    <div><h4>QUICK LINKS</h4><ul><li>Home</li><li>About us</li><li>Our Services</li><li>Latest blog</li><li>Contact Us</li></ul></div>
    <div><h4>CONTACT US</h4><ul><li>14 Harbour View Lane,<br>Nelson 7010</li><li>hello@marlowcatlodge.co.nz</li><li>021 555 014</li></ul></div>
    <div><h4>OPENING HOURS</h4><ul><li>Mon - Sat : 9.00am - 05.00pm</li><li>Sun : Closed</li></ul><h4 style="margin-top:5px">CONNECT</h4><div class="socials"><i></i><i></i><i></i></div></div>
    <div class="copyright">© Marlow Cat Lodge . All rights reserved</div>
  </footer>
</div>

<!-- ABOUT -->
<div class="page page--about">
  <header class="site-header">
    <div class="brand"><span class="brand-dot"></span>Marlow Cat Lodge</div>
    <nav class="nav"><span>Home</span><span class="active">About us</span><span>Our Services</span><span>Latest blog</span><span>Contact Us</span></nav>
    <div class="loc"><span class="pin"><svg width="5" height="5" viewBox="0 0 10 10"><path d="M5 1a3 3 0 0 1 3 3c0 2-3 5-3 5S2 6 2 4a3 3 0 0 1 3-3z" fill="#fff"/></svg></span><div><b>LOCATIONS</b>New Zealand</div></div>
  </header>
  <section class="page-hero"><div class="photo" role="img" aria-label="Caretaker with a cat beside blue cat condos"></div><div class="hero-text"><h1>ABOUT US</h1><p>Lorem ipsum dolor sit amet, consectetur adipiscing elit, sed do eiusmod tempor incididunt ut labore et dolore magna aliqua.</p></div></section>

  <section style="height:190px">
    <div class="photo blob tone-cat" style="left:46px;top:40px;width:152px;height:132px" role="img" aria-label="Cat resting inside a blue cat condo"></div>
    <div style="position:absolute;left:229px;top:62px;width:165px">
      <div class="eyebrow" style="font-size:3.8px">Introduction to Marlow Cat Lodge</div>
      <div class="h2" style="margin:2px 0 4px">Our Story</div>
      <p class="p">At Marlow Cat Lodge, we're more than just a boarding facility—we're a family-run, vet-supervised home away from home for your feline companions.</p>
      <p class="p" style="margin-top:4px">Lorem ipsum dolor sit amet, consectetur adipiscing elit, sed do eiusmod tempor incididunt ut labore et dolore magna aliqua. Quis ipsum suspendisse ultrices gravida. Risus commodo viverra maecenas accumsan lacus.</p>
    </div>
  </section>
  <section style="height:50px">
    <div style="position:absolute;left:42px;top:5px;width:360px;height:40px;background:var(--blue);border-radius:3px;display:flex;align-items:center;justify-content:space-around;color:#fff;font-size:3.8px;font-weight:500">
      <span style="display:flex;gap:4px;align-items:center"><svg width="10" height="10" viewBox="0 0 12 12"><rect x="1" y="2" width="10" height="8" fill="none" stroke="#fff"/></svg>Low-stress, boutique-<br>style boarding</span>
      <span style="display:flex;gap:4px;align-items:center"><svg width="10" height="10" viewBox="0 0 12 12"><circle cx="6" cy="6" r="4" fill="none" stroke="#fff"/></svg>Veterinary supervision<br>on-site.</span>
      <span style="display:flex;gap:4px;align-items:center"><svg width="10" height="10" viewBox="0 0 12 12"><path d="M6 1v10M1 6h10" stroke="#fff"/></svg>Special care for cats with<br>medical needs</span>
      <span style="display:flex;gap:4px;align-items:center"><svg width="10" height="10" viewBox="0 0 12 12"><path d="M2 6l3 3 5-6" fill="none" stroke="#fff"/></svg>Focus on comfort,<br>cleanliness, and safety.</span>
    </div>
  </section>
  <section style="height:355px">
    <div class="center" style="padding-top:29px"><div class="eyebrow">Meet the team</div><div class="h2" style="margin-top:2px">Our Dedicated Team</div></div>
    <div class="portrait photo round tone-face" style="left:75px;top:65px" role="img" aria-label="Portrait of the lodge veterinarian"></div>
    <div class="member" style="left:188px;top:75px"><div class="eyebrow">Meet Helena – the vet &amp; cat whisperer</div><p class="p">Dr. Helena Varga is a highly experienced veterinarian with over 20 years in small animal medicine across Europe and New Zealand. With expertise in surgery, dentistry, and laboratory diagnostics, she ensures every cat receives expert care. Whether it's a healthy, elderly, or medically fragile cat, she provides the professional attention and compassion they need.</p></div>
    <div class="portrait photo round tone-dark" style="left:275px;top:158px" role="img" aria-label="Portrait of the operations lead"></div>
    <div class="member member--right" style="left:52px;top:175px"><div class="eyebrow">Meet Tomas – the tech &amp; operations expert</div><p class="p">With a background in IT, process optimization, and management, Tomas Brecker runs the technical and organizational side of Marlow Cat Lodge. From seamless online booking to a stress-free environment, he focuses on making everything run smoothly and creating a modern, premium boarding experience.</p></div>
    <div class="portrait photo round tone-family" style="left:75px;top:250px" role="img" aria-label="Family photo by a lake"></div>
    <div class="member" style="left:188px;top:267px"><div class="eyebrow">Our family team</div><p class="p">We believe a loving environment makes all the difference. Our teenage kids are part of the team, giving the cats extra playtime, cuddles, and attention. At Marlow Cat Lodge, we're providing peace of mind for owners and a second home for their pets.</p></div>
  </section>
  <section class="cats-strip" style="height:90px"><div class="photo" style="top:20px" role="img" aria-label="Row of kittens peeking over the edge"></div></section>
  <section style="height:190px;background:var(--blue)">
    <h2 class="center" style="padding-top:30px;font-size:14px;font-weight:700;color:#fff">CUSTOMER TESTIMONIALS</h2>
    <div style="position:absolute;left:42px;top:61px;display:flex;gap:6px;align-items:flex-start">
      <div style="width:116px;height:90px;background:#fff;border-radius:3px;padding:7px;overflow:hidden"><div class="post-title" style="color:var(--blue);font-size:5px;margin:0">Ravi Kent</div><div style="color:#f2b01e;font-size:4px">★★★★★</div><p class="p" style="font-size:3.7px">Lorem ipsum dolor sit amet, consectetur adipiscing elit, sed do eiusmod tempor incididunt ut labore et dolore magna aliqua. Quis ipsum suspendisse ultrices gravida. Risus commodo viverra.</p></div>
      <div style="width:116px;height:75px;background:#fff;border-radius:3px;padding:7px;overflow:hidden"><div class="post-title" style="color:var(--blue);font-size:5px;margin:0">Nora</div><div style="color:#f2b01e;font-size:4px">★★★★★</div><p class="p" style="font-size:3.5px">Lorem ipsum dolor sit amet, consectetur adipiscing elit, sed do eiusmod tempor incididunt ut labore et dolore magna aliqua. Quis ipsum suspendisse.</p></div>
      <div style="width:116px;height:90px;background:#fff;border-radius:3px;padding:7px;overflow:hidden"><div class="post-title" style="color:var(--blue);font-size:5px;margin:0">Lena</div><div style="color:#f2b01e;font-size:4px">★★★★★</div><p class="p" style="font-size:3.7px">Lorem ipsum dolor sit amet, consectetur adipiscing elit, sed do eiusmod tempor incididunt ut labore et dolore magna aliqua. Quis ipsum suspendisse ultrices gravida. Risus commodo viverra.</p></div>
    </div>
  </section>
  <section class="cta-plain" style="height:68px"><h3>READY TO BOOK YOUR CAT'S STAY?</h3><span class="btn btn--line">Book now</span></section>
  <footer class="site-footer" style="height:123px">
    <div><div class="brand"><span class="brand-dot"></span>Marlow Cat Lodge</div><p class="p">Boutique, vet-supervised cat boarding in Nelson with calm suites and easy self check-in.</p></div>
    <div><h4>QUICK LINKS</h4><ul><li>Home</li><li>About us</li><li>Our Services</li><li>Latest blog</li><li>Contact Us</li></ul></div>
    <div><h4>CONTACT US</h4><ul><li>14 Harbour View Lane,<br>Nelson 7010</li><li>hello@marlowcatlodge.co.nz</li><li>021 555 014</li></ul></div>
    <div><h4>OPENING HOURS</h4><ul><li>Mon - Sat : 9.00am - 05.00pm</li><li>Sun : Closed</li></ul><h4 style="margin-top:5px">CONNECT</h4><div class="socials"><i></i><i></i><i></i></div></div>
    <div class="copyright">© Marlow Cat Lodge . All rights reserved</div>
  </footer>
</div>

<!-- SERVICES -->
<div class="page page--services">
  <header class="site-header">
    <div class="brand"><span class="brand-dot"></span>Marlow Cat Lodge</div>
    <nav class="nav"><span>Home</span><span>About us</span><span class="active">Our Services</span><span>Latest blog</span><span>Contact Us</span></nav>
    <div class="loc"><span class="pin"><svg width="5" height="5" viewBox="0 0 10 10"><path d="M5 1a3 3 0 0 1 3 3c0 2-3 5-3 5S2 6 2 4a3 3 0 0 1 3-3z" fill="#fff"/></svg></span><div><b>LOCATIONS</b>New Zealand</div></div>
  </header>
  <section class="page-hero"><div class="photo" role="img" aria-label="Caretaker with a cat beside blue cat condos"></div><div class="hero-text" style="width:140px"><h1>SERVICE OFFERINGS</h1><p>We offer a variety of boarding, comfort, and premium services</p></div></section>

  <section style="height:255px">
    <div class="photo round tone-cat" style="left:66px;top:27px;width:120px;height:115px" role="img" aria-label="Cat sitting in a blue cat condo"></div>
    <div style="position:absolute;left:209px;top:43px;width:180px"><div class="h2 h2--blue">Boarding Services</div><p class="p" style="margin-top:4px">Lorem ipsum dolor sit amet, consectetur adipiscing elit, sed do eiusmod tempor incididunt ut labore et dolore magna aliqua. Quis ipsum suspendisse ultrices gravida.</p><p class="p" style="margin-top:3px">Quis ipsum suspendisse ultrices gravida. Risus commodo viverra maecenas accumsan lacus vel facilisis.</p></div>
    <div class="svc-grid" style="top:158px">
      <div><h4>Standard Cat Boarding</h4><p>Spacious, full-height enclosures with cozy bedding and a cat tree.</p></div>
      <div><h4>Premium Cat Boarding</h4><p>Extra-large suites with private outdoor access and more space.</p></div>
      <div><h4>Special-Needs Boarding</h4><p>Dedicated suites for elderly or medically fragile cats.</p></div>
      <div><h4>Multi-Cat Family Boarding</h4><p>Connected suites for cats from the same household.</p></div>
      <div><h4>Short-Term Daycare</h4><p>Half-day or full-day stays for busy owners.</p></div>
      <div><h4>Post-Surgery Recovery</h4><p>Quiet space for cats needing monitored recovery.</p></div>
    </div>
  </section>

  <section style="height:345px">
    <div style="position:absolute;left:-60px;top:0;width:564px;height:345px;border-radius:50%;background:var(--light)"></div>
    <div style="position:absolute;left:66px;top:65px;width:180px"><div class="h2 h2--blue">Comfort &amp; Wellness</div><p class="p" style="margin-top:4px">Lorem ipsum dolor sit amet, consectetur adipiscing elit, sed do eiusmod tempor incididunt ut labore et dolore magna aliqua. Quis ipsum suspendisse ultrices gravida.</p><p class="p" style="margin-top:3px">Quis ipsum suspendisse ultrices gravida. Risus commodo viverra maecenas accumsan lacus vel facilisis.</p></div>
    <div class="photo round tone-kitten" style="left:263px;top:45px;width:118px;height:115px" role="img" aria-label="Kitten playing with a green ball"></div>
    <div class="svc-grid" style="top:181px">
      <div><h4>Personalized Play Sessions</h4><p>One-on-one interactive time with trained staff.</p></div>
      <div><h4>Feline Spa Experience</h4><p>Gentle brushing and coat conditioning.</p></div>
      <div><h4>Custom Hideouts</h4><p>Cozy hideaway setups for shy cats.</p></div>
      <div><h4>Live Webcam Access</h4><p>Check in on your cat anytime via webcam.</p></div>
      <div><h4>Daily Behavior Reports</h4><p>Updates on mood, appetite and activity.</p></div>
      <div><h4>Pick-Up &amp; Drop-Off</h4><p>Stress-free transport for busy owners.</p></div>
      <div><h4>Self Check-In &amp; Check-Out</h4><p>Seamless, tech-driven drop-off and pickup.</p></div>
      <div><h4>Digital Care Reports</h4><p>Daily updates with photos and notes.</p></div>
    </div>
  </section>

  <section style="height:265px">
    <div class="photo round tone-vet" style="left:66px;top:22px;width:118px;height:115px" role="img" aria-label="Veterinarian examining a cat"></div>
    <div style="position:absolute;left:209px;top:40px;width:180px"><div class="h2 h2--blue">Veterinary</div><p class="p" style="margin-top:4px">Lorem ipsum dolor sit amet, consectetur adipiscing elit, sed do eiusmod tempor incididunt ut labore et dolore magna aliqua. Quis ipsum suspendisse ultrices gravida.</p><p class="p" style="margin-top:3px">Quis ipsum suspendisse ultrices gravida. Risus commodo viverra maecenas accumsan lacus vel facilisis.</p></div>
    <div class="svc-grid" style="top:155px">
      <div><h4>Weight Management</h4><p>Tailored diet plans with intake tracking.</p></div>
      <div><h4>Dental &amp; Oral Hygiene</h4><p>Vet-led teeth checks and tartar control.</p></div>
      <div><h4>Medication Handling</h4><p>Safe handling of pills and treatments.</p></div>
      <div><h4>Hydration &amp; Supplements</h4><p>Proper hydration and vet-approved supplements.</p></div>
      <div><h4>Vaccinations &amp; Deworming</h4><p>Routine parasite prevention and boosters.</p></div>
      <div><h4>Emergency Vet Access</h4><p>Immediate care during a cat's stay.</p></div>
      <div><h4>Pain &amp; Comfort Care</h4><p>Vet-supervised pain relief and recovery.</p></div>
    </div>
  </section>
  <section class="cats-strip"><div class="photo" role="img" aria-label="Row of kittens peeking over the edge"></div></section>
  <section class="cta-band" style="height:62px"><h3>READY TO BOOK YOUR CAT'S STAY?</h3><span class="btn btn--ghost">Book now</span></section>
  <footer class="site-footer" style="height:104px;padding-top:16px">
    <div><div class="brand"><span class="brand-dot"></span>Marlow Cat Lodge</div><p class="p">Boutique, vet-supervised cat boarding in Nelson with calm suites and easy self check-in.</p></div>
    <div><h4>QUICK LINKS</h4><ul><li>Home</li><li>About us</li><li>Our Services</li><li>Latest blog</li><li>Contact Us</li></ul></div>
    <div><h4>CONTACT US</h4><ul><li>14 Harbour View Lane,<br>Nelson 7010</li><li>hello@marlowcatlodge.co.nz</li><li>021 555 014</li></ul></div>
    <div><h4>OPENING HOURS</h4><ul><li>Mon - Sat : 9.00am - 05.00pm</li><li>Sun : Closed</li></ul><h4 style="margin-top:5px">CONNECT</h4><div class="socials"><i></i><i></i><i></i></div></div>
    <div class="copyright" style="bottom:6px">© Marlow Cat Lodge . All rights reserved</div>
  </footer>
</div>

<!-- BLOG -->
<div class="page page--blog">
  <header class="site-header">
    <div class="brand"><span class="brand-dot"></span>Marlow Cat Lodge</div>
    <nav class="nav"><span>Home</span><span>About us</span><span>Our Services</span><span class="active">Latest blog</span><span>Contact Us</span></nav>
    <div class="loc"><span class="pin"><svg width="5" height="5" viewBox="0 0 10 10"><path d="M5 1a3 3 0 0 1 3 3c0 2-3 5-3 5S2 6 2 4a3 3 0 0 1 3-3z" fill="#fff"/></svg></span><div><b>LOCATIONS</b>New Zealand</div></div>
  </header>
  <section class="page-hero"><div class="photo" role="img" aria-label="Caretaker with a cat beside blue cat condos"></div><div class="hero-text"><h1>LATEST BLOG</h1><p>Lorem ipsum dolor sit amet, consectetur adipiscing elit, sed do eiusmod tempor. dolore magna aliqua.</p></div></section>
  <section style="height:315px">
    <div class="h2" style="position:absolute;left:42px;top:48px">Cat Care Tips &amp; News</div>
    <div style="position:absolute;left:42px;top:78px;width:180px;height:182px;border:.5px solid var(--line);overflow:hidden">
      <div style="height:100px;background:linear-gradient(100deg,#9fb0c0,#6c8296)" role="img" aria-label="Caretaker holding a cat in the lodge"></div>
      <div style="padding:7px 8px"><div class="post-meta"><span>● Tomas</span><span>▣ 21/03/2025</span></div><div class="post-title">Lorem ipsum dolor sit amet, consectetur adipiscing elit, sed do eiusmod</div><p class="p" style="font-size:3.5px">Lorem ipsum dolor sit amet, consectetur adipiscing elit, sed do eiusmod tempor incididunt ut labore et dolore magna aliqua. Quis ipsum suspendisse ultrices gravida.</p></div>
    </div>
    <div style="position:absolute;left:227px;top:78px;width:180px">
      <div class="mini"><div class="thumb tone-cat" role="img" aria-label="Cat in a blue condo"></div><div style="padding:3px"><div class="post-meta"><span>● Tomas</span><span>▣ 21/03/2025</span></div><div class="post-title">Ipsum dolor sit amet eiusmod</div><p class="p">Lorem ipsum dolor sit amet, consectetur adipiscing elit, sed do eiusmod tempor incididunt ut labore.</p></div></div>
      <div class="mini"><div class="thumb tone-kitten" role="img" aria-label="Kitten with a green ball"></div><div style="padding:3px"><div class="post-meta"><span>● Tomas</span><span>▣ 21/03/2025</span></div><div class="post-title">Ipsum dolor sit amet eiusmod</div><p class="p">Lorem ipsum dolor sit amet, consectetur adipiscing elit, sed do eiusmod tempor incididunt ut labore.</p></div></div>
      <div class="mini"><div class="thumb tone-vet" role="img" aria-label="Vet holding a cat"></div><div style="padding:3px"><div class="post-meta"><span>● Tomas</span><span>▣ 21/03/2025</span></div><div class="post-title">Ipsum dolor sit amet eiusmod</div><p class="p">Lorem ipsum dolor sit amet, consectetur adipiscing elit, sed do eiusmod tempor incididunt ut labore.</p></div></div>
    </div>
    <div style="position:absolute;left:0;right:0;top:292px;display:flex;justify-content:center;align-items:center;gap:3px;font-size:3.8px;color:#fff">
      <span style="width:9px;height:9px;border-radius:50%;background:var(--blue-deep);display:flex;align-items:center;justify-content:center">1</span>
      <span style="width:9px;height:9px;border-radius:50%;background:#8795a3;display:flex;align-items:center;justify-content:center">2</span>
      <span style="color:#3b4a5a;letter-spacing:1px">.............</span>
      <span style="width:9px;height:9px;border-radius:50%;background:#8795a3;display:flex;align-items:center;justify-content:center">5</span>
    </div>
  </section>
  <section class="cats-strip" style="height:83px"><div class="photo" style="top:10px" role="img" aria-label="Row of kittens peeking over the edge"></div></section>
  <section class="cta-band" style="height:76px"><h3>READY TO BOOK YOUR CAT'S STAY?</h3><span class="btn btn--ghost">Book now</span></section>
  <footer class="site-footer" style="height:121px">
    <div><div class="brand"><span class="brand-dot"></span>Marlow Cat Lodge</div><p class="p">Boutique, vet-supervised cat boarding in Nelson with calm suites and easy self check-in.</p></div>
    <div><h4>QUICK LINKS</h4><ul><li>Home</li><li>About us</li><li>Our Services</li><li>Latest blog</li><li>Contact Us</li></ul></div>
    <div><h4>CONTACT US</h4><ul><li>14 Harbour View Lane,<br>Nelson 7010</li><li>hello@marlowcatlodge.co.nz</li><li>021 555 014</li></ul></div>
    <div><h4>OPENING HOURS</h4><ul><li>Mon - Sat : 9.00am - 05.00pm</li><li>Sun : Closed</li></ul><h4 style="margin-top:5px">CONNECT</h4><div class="socials"><i></i><i></i><i></i></div></div>
    <div class="copyright">© Marlow Cat Lodge . All rights reserved</div>
  </footer>
</div>

<!-- CONTACT -->
<div class="page page--contact">
  <header class="site-header">
    <div class="brand"><span class="brand-dot"></span>Marlow Cat Lodge</div>
    <nav class="nav"><span>Home</span><span>About us</span><span>Our Services</span><span>Latest blog</span><span class="active">Contact Us</span></nav>
    <div class="loc"><span class="pin"><svg width="5" height="5" viewBox="0 0 10 10"><path d="M5 1a3 3 0 0 1 3 3c0 2-3 5-3 5S2 6 2 4a3 3 0 0 1 3-3z" fill="#fff"/></svg></span><div><b>LOCATIONS</b>New Zealand</div></div>
  </header>
  <section class="page-hero" style="height:166px"><div class="photo" role="img" aria-label="Caretaker with a cat beside blue cat condos"></div><div class="hero-text" style="width:130px"><h1>CONTACT US</h1><p>Lorem ipsum dolor sit amet, consectetur adipiscing elit, sed do eiusmod tempor incididunt</p></div></section>
  <section style="height:180px">
    <div style="position:absolute;left:70px;top:47px">
      <div class="eyebrow" style="font-size:4.6px;margin-bottom:8px">Contact information</div>
      <div class="info-item"><span class="pin"><svg width="6" height="6" viewBox="0 0 10 10"><path d="M5 1a3 3 0 0 1 3 3c0 2-3 5-3 5S2 6 2 4a3 3 0 0 1 3-3z" fill="#fff"/></svg></span><div><b>Location :</b><span>14 Harbour View Lane, Nelson 7010</span></div></div>
      <div class="info-item"><span class="pin"><svg width="6" height="6" viewBox="0 0 10 10"><path d="M2 1h2l1 2-1 1a6 6 0 0 0 2 2l1-1 2 1v2c-4 0-7-3-7-7z" fill="#fff"/></svg></span><div><b>Phone Number :</b><span>021 555 014</span></div></div>
      <div class="info-item"><span class="pin"><svg width="6" height="6" viewBox="0 0 10 10"><rect x="1" y="2" width="8" height="6" fill="none" stroke="#fff"/><path d="M1 2l4 3 4-3" fill="none" stroke="#fff"/></svg></span><div><b>Email Us :</b><span>hello@marlowcatlodge.co.nz</span></div></div>
      <div class="info-item"><span class="pin"><svg width="6" height="6" viewBox="0 0 10 10"><circle cx="5" cy="5" r="3.5" fill="none" stroke="#fff"/><path d="M5 3v2h2" stroke="#fff" fill="none"/></svg></span><div><b>Hours :</b><span>Mon - Sat : 9.00am - 05.00pm<br>Sun : Closed</span></div></div>
    </div>
    <div class="photo tone-map" style="left:233px;top:35px;width:135px;height:125px;border-radius:50%" role="img" aria-label="Street map showing the lodge location with a marker"></div>
  </section>
  <section class="cats-strip" style="height:95px"><div class="photo" style="top:15px" role="img" aria-label="Row of kittens peeking over the edge"></div></section>
  <section class="prebook" style="height:223px;padding-top:28px">
    <h2>CONTACT &amp; PRE-BOOK</h2>
    <div class="form-grid" style="margin-top:13px">
      <div class="field">Your name*</div><div class="field">Your cats name*</div><div class="field">Your email address*</div><div class="field">Your email address*</div>
      <div class="field field--half">Pre book a stay from <span>▢</span></div><div class="field field--half">Pre book a stay until <span>▢</span></div>
    </div>
    <div class="option-title">Boarding option</div>
    <div class="options"><span>Standard Condo ($30 / day)</span><span>Premium Condo ($50 / day)</span></div>
    <div class="textarea">General enquiry / additional information?<small>e.g. multiple cats, additional services...</small></div>
    <span class="submit">SUBMIT</span>
  </section>
  <footer class="site-footer" style="height:108px;padding-top:18px">
    <div><div class="brand"><span class="brand-dot"></span>Marlow Cat Lodge</div><p class="p">Boutique, vet-supervised cat boarding in Nelson with calm suites and easy self check-in.</p></div>
    <div><h4>QUICK LINKS</h4><ul><li>Home</li><li>About us</li><li>Our Services</li><li>Latest blog</li><li>Contact Us</li></ul></div>
    <div><h4>CONTACT US</h4><ul><li>14 Harbour View Lane,<br>Nelson 7010</li><li>hello@marlowcatlodge.co.nz</li><li>021 555 014</li></ul></div>
    <div><h4>OPENING HOURS</h4><ul><li>Mon - Sat : 9.00am - 05.00pm</li><li>Sun : Closed</li></ul><h4 style="margin-top:5px">CONNECT</h4><div class="socials"><i></i><i></i><i></i></div></div>
    <div class="copyright" style="bottom:7px">© Marlow Cat Lodge . All rights reserved</div>
  </footer>
</div>

</div>
</body>
</html>
```